Card design for Heating and Cooling company

this is for a heating and cooling company we recently updated our logo and need to update our cards. We attached our logo so you can incorporate it into the card. We specialize in residential and commercial furnace and air condition repairs. Have been in business since 2014.

Phone number 555.284.9137

We need the following phrases
:Repairs, Installations, and maintenance
:Quality work at reasonable prices
:residential/commercial
:Licensed &Insured
:Email Pinegrovehvac47@mailbox-example.com
Name: Teodor K (Ted)
Also on back side I would like my logo with wording :Thank you for your business and refferal

Industry/Entity Type

Hvac

Contact Information for Business Card

:residential/commercial
:Licensed & Insured
Name: Teodor K (Ted)
Number:555.284.9136

Requirements
Must have
• Blue and red colors
Nice to have
• Maybe a pic of a furnace or air conditioner

```html
<!DOCTYPE html>
<html lang="en">
<head>
<meta charset="utf-8">
<title>Pinegrove Heating &amp; Cooling – Business Card</title>
<link href="https://fonts.googleapis.com/css2?family=Jost:wght@400;500&display=swap" rel="stylesheet">
<style>
  :root {
    --backdrop: #e7e7e7;
    --heat: #e64f1a;
    --heat-soft: #f0a184;
    --cool: #1f73c2;
    --cool-soft: #a9cbea;
    --paper: #ffffff;
    --ink: #1b1b1b;
  }
  * { margin: 0; padding: 0; box-sizing: border-box; }
  html, body {
    width: 1200px;
    height: 800px;
    overflow: hidden;
    background: var(--backdrop);
    font-family: "Jost", sans-serif;
    color: var(--ink);
  }
  .sheet {
    width: 1200px;
    height: 800px;
    display: flex;
    align-items: center;
    justify-content: center;
    gap: 60px;
  }
  .card {
    position: relative;
    width: 520px;
    height: 297px;
    overflow: hidden;
  }
  .card--back {
    background: linear-gradient(to bottom, var(--heat) 0%, var(--heat-soft) 50%, var(--paper) 100%);
    display: flex;
    flex-direction: column;
    align-items: center;
  }
  .card--front {
    background: linear-gradient(to bottom, var(--paper) 0%, var(--cool-soft) 45%, var(--cool) 100%);
  }
  .brand {
    display: flex;
    align-items: center;
    gap: 10px;
  }
  .brand__mark {
    width: 26px;
    height: 26px;
    border-radius: 50%;
    background: var(--cool);
    flex: none;
  }
  .brand__name {
    font-weight: 500;
    color: var(--ink);
    line-height: 1.15;
    letter-spacing: 0.02em;
  }
  .card--back .brand {
    margin-top: 105px;
  }
  .card--back .brand__name { font-size: 24px; }
  .thanks {
    position: absolute;
    bottom: 34px;
    left: 0;
    right: 0;
    text-align: center;
    font-size: 19px;
    font-weight: 400;
  }
  .card--front .brand {
    position: absolute;
    left: 26px;
    top: 128px;
    width: 168px;
    gap: 8px;
  }
  .card--front .brand__mark { width: 20px; height: 20px; }
  .card--front .brand__name { font-size: 16px; }
  .details {
    position: absolute;
    left: 208px;
    top: 52px;
    right: 16px;
  }
  .details__name {
    font-size: 22px;
    font-weight: 500;
    color: var(--heat);
    margin-bottom: 10px;
  }
  .details__contact {
    font-size: 17px;
    line-height: 1.35;
    margin-bottom: 16px;
    white-space: nowrap;
  }
  .details__services {
    list-style: none;
    font-size: 15px;
    line-height: 1.4;
  }
</style>
</head>
<body>
  <main class="sheet">
    <section class="card card--back" aria-label="Card back">
      <div class="brand">
        <span class="brand__mark"></span>
        <span class="brand__name">PINEGROVE<br>Heating &amp; Cooling</span>
      </div>
      <p class="thanks">Thank you for your business and refferal</p>
    </section>

    <section class="card card--front" aria-label="Card front">
      <div class="brand">
        <span class="brand__mark"></span>
        <span class="brand__name">PINEGROVE<br>Heating &amp; Cooling</span>
      </div>
      <div class="details">
        <h1 class="details__name">Teodor K (Ted)</h1>
        <p class="details__contact">555 284 9136<br>Pinegrovehvac47@mailbox-example.com</p>
        <ul class="details__services">
          <li>Repairs, Installations, and maintenance</li>
          <li>Quality work at reasonable prices</li>
          <li>residential/commercial</li>
          <li>Licensed &amp; Insured</li>
        </ul>
      </div>
    </section>
  </main>
</body>
</html>
```